Hochzeitseinladung
Zielgruppe
Gastronomie - Zielgruppe ist ein Hochzeitspaar, welches bei uns feiert. Wir dürfen Ihre Hochzeitseinladung entwerfen.
Aufgabenstellung
Den Textvorschlag des Brautpaares findet Ihr im Anhang. Das Thema der Hochzeit ist AMORE.
1. Die Hochzeitseinladung darf gerne kreativ gestaltet sein, vielleicht in Form des Moodboard-Bildes im Anhang? Jonas hat braune Haare und Locken und Frieda lange braune Haare. Beide tragen eine Brille.
Das Hochzeitspaar hat noch einen kleinen braunen Zwergpudel 'Tibo', vielleicht findet er auch noch Platz auf der Einladungskarte ;-).
2. Als Alternativ-Vorschlag wäre ein klassisches Design auf zB geprägtem Papier toll.
3. Etwas Schlichtes mit einem Neon-Accessoire würde das Hochzeitspaar auch gut finden. Zb brauner Karton mit einem Neonband.

```html
<!DOCTYPE html>
<html lang="de">
<head>
<meta charset="utf-8">
<title>Antwortkarte – Frieda + Jonas</title>
<link rel="stylesheet" href="https://fonts.googleapis.com/css2?family=Montserrat:wght@400;500;700&display=swap">
<style>
  :root {
    --backdrop: #e2cfc2;
    --illustration-tone: #e9d9cf;
    --illustration-light: #efe2da;
    --card: #ffffff;
    --ink: #3b3a3a;
    --ink-soft: #555353;
    --rule: #6d6b6b;
    --dots: #a9a6a4;
    --heading: #ffffff;
  }
  * { margin: 0; padding: 0; box-sizing: border-box; }
  html, body { width: 1200px; height: 1200px; overflow: hidden; }
  body {
    position: relative;
    background: var(--backdrop);
    font-family: "Montserrat", sans-serif;
    color: var(--ink);
  }
  .section-title {
    position: absolute;
    left: 640px; top: 186px;
    font-weight: 700;
    font-size: 17px;
    letter-spacing: 0.12em;
    font-variant: small-caps;
    color: var(--heading);
  }
  .pet-illustration {
    position: absolute;
    left: 0; top: 435px;
    width: 578px; height: 765px;
    background: radial-gradient(ellipse at 50% 35%, var(--illustration-light) 0%, var(--illustration-tone) 45%, var(--backdrop) 80%);
  }
  .rsvp-card {
    position: absolute;
    left: 640px; top: 265px;
    width: 431px; height: 654px;
    background: var(--card);
    box-shadow: 2px 4px 6px rgba(0,0,0,0.22);
  }
  .rsvp-card > * { position: absolute; line-height: 1; }
  .monogram { left: 200px; top: 60px; width: 108px; height: 108px; }
  .monogram text { font-family: "Montserrat", sans-serif; font-size: 10.5px; letter-spacing: 2.4px; fill: #1c1c1c; font-weight: 500; }
  .side-rule { left: 372px; top: 47px; width: 1px; height: 136px; background: var(--rule); }
  .side-label {
    left: 366px; top: 215px;
    width: 12px;
    font-size: 11px;
    font-weight: 500;
    text-align: center;
    line-height: 18.6px;
  }
  .label {
    font-size: 9.5px;
    font-weight: 700;
    letter-spacing: 0.32em;
    text-transform: uppercase;
    color: var(--ink);
  }
  .detail {
    font-size: 9.5px;
    font-weight: 400;
    letter-spacing: 0.32em;
    text-transform: uppercase;
    color: var(--ink-soft);
  }
  .deadline-label { left: 43px; top: 211px; }
  .deadline-date { left: 43px; top: 230px; font-size: 11.5px; letter-spacing: 0.18em; }
  .deadline-date .sc { font-size: 9.5px; letter-spacing: 0.3em; }
  .name-label { left: 43px; top: 292px; }
  .fill-line { left: 43px; height: 0; border-top: 1.5px dotted var(--dots); }
  .name-line-1 { top: 334px; width: 263px; }
  .name-line-2 { top: 367px; width: 263px; }
  .choice-mark {
    width: 9px; height: 9px;
    border: 1px solid var(--ink);
    border-radius: 50%;
    left: 42px;
  }
  .accept-mark { top: 414px; }
  .decline-mark { top: 475px; }
  .accept-label { left: 61px; top: 414px; }
  .guest-count { left: 61px; top: 433px; display: flex; align-items: flex-end; gap: 8px; }
  .guest-count .blank { width: 28px; border-top: 1.5px dotted var(--dots); margin-bottom: 0; }
  .guest-count .detail { font-size: 10px; }
  .decline-label { left: 61px; top: 475px; }
  .decline-note { left: 61px; top: 496px; }
  .diet-label { left: 43px; top: 556px; }
  .diet-line { top: 599px; width: 350px; }
</style>
</head>
<body>
  <h1 class="section-title">Antwortkarte</h1>

  <div class="pet-illustration" role="img" aria-label="Feine Linienzeichnung des braunen Zwergpudels Tibo mit Halsband, hell auf dem Hintergrund"></div>

  <section class="rsvp-card">
    <svg class="monogram" viewBox="0 0 108 108" aria-label="Frieda + Jonas 20.4.2024">
      <defs>
        <path id="monogram-ring" d="M54,54 m-44,0 a44,44 0 1,1 88,0 a44,44 0 1,1 -88,0"/>
      </defs>
      <text><textPath href="#monogram-ring" startOffset="2%">FRIEDA + JONAS 20.4.2024 •</textPath></text>
    </svg>

    <div class="side-rule"></div>
    <div class="side-label">R<br>S<br>V<br>P</div>

    <p class="label deadline-label">Sendet diese Karte bis zum</p>
    <p class="detail deadline-date">30. <span class="sc">April</span> 2024</p>

    <p class="label name-label">Name/n</p>
    <div class="fill-line name-line-1"></div>
    <div class="fill-line name-line-2"></div>

    <span class="choice-mark accept-mark"></span>
    <p class="label accept-label">Am Start</p>
    <div class="guest-count"><span class="blank"></span><span class="detail">Person/en</span></div>

    <span class="choice-mark decline-mark"></span>
    <p class="label decline-label">So schade</p>
    <p class="detail decline-note">Da steht bereits was im Kalender</p>

    <p class="label diet-label">Allergien/ Unverträglichkeiten</p>
    <div class="fill-line diet-line"></div>
  </section>
</body>
</html>
```